Cobalto Grande

I want a glossy card on both sides. We sell underwater LED lights for water craft

we sell custom audio enclosures for automobile, boats and atv's.

view our websites for any other pictures you may think are better suited.

Industry/Entity Type

Audio

Contact Information for Business Card

Email address: CobaltoGrande@mailvista.example
Website: www.hullglowtap.example
underwater LED lighting for watercraft
boat drain plug lights
phone number: 555-271-0648

other side of card:
email address the same
website: www.versatilesoundshells.example
speaker enclosures, auto, boat and atv
same phone number

```html
<!DOCTYPE html>
<html lang="en">
<head>
<meta charset="utf-8">
<title>Cobalto Grande – Business Cards</title>
<link rel="stylesheet" href="https://fonts.googleapis.com/css2?family=Montserrat:wght@400;700;800&display=swap">
<style>
  :root {
    --page-bg: #ffffff;
    --ink: #3b3b3b;
    --ink-strong: #1f1f1f;
    --accent-red: #ee1c25;
    --steel-center: #ffffff;
    --steel-edge: #b3bcbc;
    --sage-center: #fbfbf6;
    --sage-edge: #c7c7a7;
  }
  * { margin: 0; padding: 0; box-sizing: border-box; }
  html, body {
    width: 1200px;
    height: 1000px;
    overflow: hidden;
    background: var(--page-bg);
  }
  .sheet {
    position: relative;
    width: 1200px;
    height: 1000px;
  }
  .card {
    position: absolute;
    left: 310px;
    width: 579px;
    height: 340px;
    font-family: "Montserrat", Arial, sans-serif;
    color: var(--ink);
    text-align: center;
  }
  .card--lights {
    top: 121px;
    background: radial-gradient(ellipse 62% 78% at 50% 48%, var(--steel-center) 0%, #e4e7e7 45%, var(--steel-edge) 100%);
  }
  .card--audio {
    top: 539px;
    background: radial-gradient(ellipse 62% 78% at 50% 48%, var(--sage-center) 0%, #e6e6d6 45%, var(--sage-edge) 100%);
  }
  .brand {
    position: absolute;
    left: 0;
    right: 0;
    top: 40px;
    display: flex;
    flex-direction: column;
    align-items: center;
  }
  .brand__dot {
    width: 48px;
    height: 48px;
    border-radius: 50%;
    background: var(--accent-red);
    margin-bottom: 16px;
  }
  .brand__name {
    font-weight: 800;
    font-size: 34px;
    line-height: 36px;
    letter-spacing: 0.5px;
    text-transform: uppercase;
    color: var(--ink);
  }
  .contact {
    position: absolute;
    left: 0;
    right: 0;
    top: 248px;
    list-style: none;
  }
  .contact__service {
    font-weight: 800;
    font-size: 14px;
    line-height: 18px;
    letter-spacing: 0.6px;
    color: var(--ink-strong);
    text-transform: uppercase;
  }
  .contact__line {
    font-weight: 400;
    font-size: 14.5px;
    line-height: 18px;
    letter-spacing: 0.9px;
    text-transform: uppercase;
  }
</style>
</head>
<body>
<main class="sheet">
  <section class="card card--lights">
    <div class="brand">
      <span class="brand__dot"></span>
      <div class="brand__name">Cobalto<br>Grande</div>
    </div>
    <ul class="contact">
      <li class="contact__service">Professional LED Lights</li>
      <li class="contact__line">www.hullglowtap.example</li>
      <li class="contact__line">CobaltoGrande@mailvista.example</li>
      <li class="contact__line">555-271-0648</li>
    </ul>
  </section>

  <section class="card card--audio">
    <div class="brand">
      <span class="brand__dot"></span>
      <div class="brand__name">Cobalto<br>Grande</div>
    </div>
    <ul class="contact">
      <li class="contact__service">Professional Car Audio</li>
      <li class="contact__line">www.versatilesoundshells.example</li>
      <li class="contact__line">CobaltoGrande@mailvista.example</li>
      <li class="contact__line">555-271-0648</li>
    </ul>
  </section>
</main>
</body>
</html>
```